Web Design Project

This web site is to be designed for a popular Cambodian singer, Vanny Kolthida. Web site name "Vanny Kolthida".

The purpose is to keep her fans update with the latest of her entertainment career and invite them to help raising fund for Lotus Bridge Youth Fund.

In addition to other normal pages such as HOME, ABOUT... This web site must be:
1. able to link to Dropshipers and add Products
2. able to donate (accept Major Credit Cards or PayVira)
3. able to purchase products (accept Major Credit Cards or PayVira)
4. able to video live chat with Vanny Kolthida
5. able to book appointment on her calendar

Here is a sample of the web site:
http://pralay82.sitebuildo.example/vanny-kol-thida

Please call me if you need any clarification at 1-555-281-3097 or leave your number for me to call you back.

Thank you

Dara

Target Market(s)

Cambodian living abroad

Industry/Entity Type

Entertainment

Requirements
Must have
• 1. able to link to Dropshipers and add Products
2. able to Donate (accept Major Credit Cards or PayVira)

```html
<!DOCTYPE html>
<html lang="en">
<head>
<meta charset="utf-8">
<title>Vanny Kolthida</title>
<link href="https://fonts.googleapis.com/css2?family=Ubuntu:ital,wght@0,400;0,500;0,700;1,400&display=swap" rel="stylesheet">
<style>
:root{
  --red-deep:#4a0606;
  --red-mid:#7a0d0d;
  --red-hi:#9c1414;
  --black:#0d0d0d;
  --footer:#161616;
  --gold:#f2c94c;
  --gold-btn:#e8c14a;
  --orange:#e0531c;
  --orange-hi:#f06a2a;
  --text:#f2f2f2;
  --muted:#bdbdbd;
  --nav-bg:#e8ddc9;
  --nav-text:#6a1a0c;
  --line:#3a3a3a;
}
*{box-sizing:border-box;margin:0;padding:0}
html,body{width:924px;height:1200px;overflow:hidden}
body{position:relative;font-family:Arial,Helvetica,sans-serif;color:var(--text);
  background:linear-gradient(180deg,var(--red-deep) 0,var(--red-mid) 180px,#5e0909 404px,#2c0404 404px,#2c0404 510px,var(--red-hi) 510px,#6a0b0b 640px,#1a0404 820px,var(--black) 940px,var(--footer) 940px,var(--footer) 1144px,var(--black) 1144px)}
.abs{position:absolute}
.ubuntu{font-family:'Ubuntu',sans-serif}

.top-links{right:100px;top:12px;font-size:10px;font-weight:bold;color:#fff}
.site-title{left:100px;top:36px;font-family:'Ubuntu',sans-serif;font-weight:500;font-size:32px;color:#f4f4f4;text-shadow:0 2px 3px rgba(0,0,0,.6)}
.share{top:53px;display:flex;align-items:center;gap:3px;font-size:9px}
.share .btn{background:#f3f3f3;color:#333;border:1px solid #aaa;border-radius:2px;padding:1px 5px}
.share .count{background:#fff;color:#333;border:1px solid #bbb;border-radius:2px;padding:1px 4px}

.main-nav{left:100px;top:102px;width:724px;height:39px;border-radius:5px;background:linear-gradient(#f6efe0,var(--nav-bg) 60%,#c9b99d);box-shadow:0 3px 6px rgba(0,0,0,.5)}
.main-nav a{position:absolute;top:11px;font-family:'Ubuntu',sans-serif;font-size:14.5px;color:var(--nav-text);text-decoration:none}
.nav-sep{position:absolute;top:8px;width:1px;height:23px;background:#bfae90}
.search{position:absolute;left:557px;top:8px;width:153px;height:23px;background:#fff;border:1px solid #9c8c70;border-radius:3px;font-size:10px;font-style:italic;color:#888;padding:5px 9px}
.search svg{position:absolute;right:6px;top:3px}

.hero{left:100px;top:156px;width:724px;height:284px;background:linear-gradient(90deg,#5e6f8c,#8e9fc0 45%,#9fb0cf);border:4px solid #3c0707}
.hero-photo{left:0;top:0;width:380px;height:276px;background:radial-gradient(ellipse at 45% 55%,#c99a86 0,#8a6a66 35%,#1e2230 70%,transparent 90%)}
.hero-text{left:386px;top:54px;font-family:'Ubuntu',sans-serif;font-weight:500;font-size:32px;line-height:40px;color:#fff;text-shadow:0 2px 3px rgba(0,0,0,.4)}
.hero-arrow{top:228px;width:30px;height:30px;border-radius:3px;background:linear-gradient(#f4f4f4,#bdbdbd);border:1px solid #777;display:flex;align-items:center;justify-content:center}

.cta-text{left:134px;top:466px;font-family:'Ubuntu',sans-serif;font-size:14.5px;color:#f2f2f2}
.donate-btn{left:638px;top:460px;width:152px;height:33px;border-radius:3px;background:linear-gradient(#f8da6a,var(--gold-btn) 60%,#c99b25);color:#3a2000;font-family:'Ubuntu',sans-serif;font-weight:500;font-size:18px;display:flex;align-items:center;justify-content:center}

h2{font-family:'Ubuntu',sans-serif;font-weight:400;color:var(--gold);font-size:20px}
.welcome-box{left:100px;top:518px;width:231px;height:300px;border:1px solid #5b2a2a;border-radius:3px;background:rgba(0,0,0,.45)}
.welcome-box h2{position:absolute;left:17px;top:10px}
.welcome-photo{left:18px;top:49px;width:194px;height:95px;border:3px solid #fff;background:linear-gradient(120deg,#c5b020,#b88a60 45%,#d95090)}
.welcome-copy{left:12px;top:152px;width:207px;text-align:center;font-size:9.6px;line-height:17.6px;color:#eee}
.btn-orange{background:linear-gradient(var(--orange-hi),var(--orange));border-radius:2px;color:#fff;font-weight:bold;font-size:11px;display:flex;align-items:center;justify-content:center;font-family:'Ubuntu',sans-serif}

.newsletter-title{left:99px;top:838px}
.email{left:100px;top:871px;width:231px;height:19px;border:1px solid #555;border-radius:3px;background:#1c1c1c;font-size:9px;font-style:italic;color:#888;padding:4px 8px}
.subscribe{left:270px;top:904px;width:60px;height:20px;background:#555;border-radius:2px;color:#eee;font-family:'Ubuntu',sans-serif;font-size:11px;display:flex;align-items:center;justify-content:center}

.products-title{left:372px;top:529px}
.circle-arrow{top:532px;width:24px;height:24px;border-radius:50%;background:#eee;border:1px solid #999;display:flex;align-items:center;justify-content:center}
.product{top:567px;width:138px}
.product .thumb{height:95px;border:2px solid #fff}
.product .name{margin-top:8px;text-align:center;font-family:'Ubuntu',sans-serif;font-size:11.5px;color:var(--gold)}
.product .price{margin-top:5px;display:flex;justify-content:center;gap:20px;font-family:'Ubuntu',sans-serif;font-size:13.5px}
.product .old{color:var(--gold);text-decoration:line-through}
.product .details{margin:5px auto 0;width:66px;height:19px}

.rule-h{left:372px;top:755px;width:452px;height:1px;background:#666}
.rule-v{left:595px;top:776px;width:1px;height:148px;background:#444}
.video-title{left:375px;top:766px}
.video{left:372px;top:796px;width:192px;height:120px;border:1px solid #555;background:linear-gradient(135deg,#2a2e38,#4a4f5c 50%,#1d2028);display:flex;align-items:center;justify-content:center;font-family:'Ubuntu',sans-serif;font-size:13px;color:#fff}
.video svg{position:absolute;left:83px;top:45px}
.video span{position:relative}
.appt-title{left:623px;top:766px}
.calendar{left:630px;top:798px;width:194px;height:120px;border:1px solid #666;border-radius:3px;background:linear-gradient(#2a2a2a,#1a1410)}
.calendar .head{height:15px;background:linear-gradient(#5b5b5b,#3a3a3a);text-align:center;font-family:'Ubuntu',sans-serif;font-size:11px;color:#eee;line-height:15px}
.cal-grid{display:grid;grid-template-columns:repeat(7,24px);padding:6px 0 0 11px;row-gap:3px;font-size:9px;text-align:center;color:#eee;font-family:'Ubuntu',sans-serif}
.cal-grid .dow{color:var(--orange);font-weight:bold}
.cal-grid .mark{background:#f7d10a;color:#222;font-weight:bold;width:14px;margin:0 auto}

.footer-col h3{font-family:'Ubuntu',sans-serif;font-weight:400;font-size:14.5px;color:var(--gold)}
.col-rule{width:1px;background:#333;top:956px;height:168px}
.f-line{height:1px;background:#3a3a3a}
.testimonial{left:100px;top:990px;width:214px;font-size:10.4px;line-height:14px;text-align:justify;color:#eee}
.quote{color:var(--orange);font-family:Georgia,serif;font-size:20px;font-weight:bold;line-height:10px}
.foot-link{font-size:9.6px;color:var(--gold)}
.news-date{font-family:'Ubuntu',sans-serif;font-style:italic;font-size:18px;line-height:16px;color:#aaa;text-align:center;width:40px}
.news-text{font-size:10px;line-height:14px;color:#eee;text-align:justify;width:185px}
.social{top:986px;width:37px;height:36px;border-radius:4px;background:linear-gradient(#f08a3a,#c95a18);border:1px solid #8a3a10;font-family:'Ubuntu',sans-serif;font-size:8.5px;color:#fff;display:flex;align-items:center;justify-content:center}
.pay-badge{left:646px;top:1082px;width:126px;height:44px;background:#fbf5e6;border:2px solid #e6d6b0;padding:3px 6px}
.pay-badge .brand{font-family:'Ubuntu',sans-serif;font-weight:700;font-size:13px;color:#1a3a7a;text-align:center}
.pay-badge .cards{display:flex;gap:4px;justify-content:center;margin-top:3px}
.pay-badge .cards i{display:block;width:22px;height:14px;background:#c9c0aa;border-radius:2px}
.copyright{left:0;width:924px;top:1156px;text-align:center;font-size:8.5px;line-height:12px;color:#ddd}
.copyright b{font-weight:normal;color:var(--orange-hi)}
</style>
</head>
<body>

<div class="abs top-links">Home &nbsp;/&nbsp; Register &nbsp;/&nbsp; Login &nbsp;/&nbsp; SiteMap</div>
<h1 class="abs site-title">Vanny Kolthida</h1>
<div class="abs share" style="left:632px"><span class="btn">Share</span><span class="count">3k</span></div>
<div class="abs share" style="left:696px"><span class="btn">Post</span><span class="count">316</span></div>
<div class="abs share" style="left:773px"><span class="btn">Plus</span><span class="count">81</span></div>

<nav class="abs main-nav">
  <a style="left:18px">HOME</a><span class="nav-sep" style="left:72px"></span>
  <a style="left:87px">ABOUT US</a><span class="nav-sep" style="left:170px"></span>
  <a style="left:182px">PRODUCTS</a><span class="nav-sep" style="left:269px"></span>
  <a style="left:279px">FEEDBACK</a><span class="nav-sep" style="left:365px"></span>
  <a style="left:380px">DONATE</a><span class="nav-sep" style="left:446px"></span>
  <a style="left:454px">CONTACT US</a>
  <div class="search">Search...
    <svg width="18" height="16" viewBox="0 0 18 16"><circle cx="7" cy="7" r="5" fill="none" stroke="#222" stroke-width="2"/><line x1="11" y1="10.5" x2="16" y2="15" stroke="#222" stroke-width="2.5"/></svg>
  </div>
</nav>

<section class="abs hero">
  <div class="abs hero-photo" role="img" aria-label="Portrait photo of the singer with dark curly hair"></div>
  <p class="abs hero-text">Our Purpose<br>to help raising fund<br>for Lotus Bridge<br>Youth Fund.....</p>
  <div class="abs hero-arrow" style="left:636px"><svg width="16" height="12"><path d="M0 6 L7 0 V4 H16 V8 H7 V12Z" fill="#333"/></svg></div>
  <div class="abs hero-arrow" style="left:672px"><svg width="16" height="12"><path d="M16 6 L9 0 V4 H0 V8 H9 V12Z" fill="#333"/></svg></div>
</section>

<p class="abs cta-text">Aliquam ullamcorper tempor felis, nec condimentum odio aliquet vitae.</p>
<div class="abs donate-btn">DONATE NOW!</div>

<section class="abs welcome-box">
  <h2>Welcome to My Site !</h2>
  <div class="abs welcome-photo" role="img" aria-label="Photo of the singer performing with a microphone"></div>
  <p class="abs welcome-copy">Lorem ipsum dolor sit amet, consec tetuer adipiscing elit. Praesent vestibulum mo lestie lacus. Aenean nonummy hendrerit mauris. Phasellus porta. Fusce suscipit varius mi. Cum sociis natoque penatibuset magnis dis parturient montes......</p>
  <div class="abs btn-orange" style="left:82px;top:267px;width:66px;height:19px">Read More</div>
</section>

<h2 class="abs newsletter-title">Newletter SignUp</h2>
<div class="abs email">Enter E-mail Address</div>
<div class="abs subscribe">Subscribe</div>

<h2 class="abs products-title">Our Products</h2>
<div class="abs circle-arrow" style="left:772px"><svg width="8" height="10"><path d="M7 0 L1 5 L7 10" fill="none" stroke="#333" stroke-width="2"/></svg></div>
<div class="abs circle-arrow" style="left:800px"><svg width="8" height="10"><path d="M1 0 L7 5 L1 10" fill="none" stroke="#333" stroke-width="2"/></svg></div>

<div class="abs product" style="left:373px">
  <div class="thumb" role="img" aria-label="Product photo: model in white headwrap" style="background:linear-gradient(135deg,#6a3a1c,#b07a52 50%,#4a2a14)"></div>
  <div class="name">Product Name</div>
  <div class="price"><span>$9.99</span><span class="old">$12.99</span></div>
  <div class="details btn-orange">Details</div>
</div>
<div class="abs product" style="left:529px">
  <div class="thumb" role="img" aria-label="Product photo: black and white fashion portrait" style="background:linear-gradient(135deg,#d8d8d8,#6a6a6a 50%,#eee)"></div>
  <div class="name">Product Name</div>
  <div class="price"><span>$9.99</span><span class="old">$12.99</span></div>
  <div class="details btn-orange">Details</div>
</div>
<div class="abs product" style="left:687px">
  <div class="thumb" role="img" aria-label="Product photo: model in black outfit outdoors" style="background:linear-gradient(180deg,#3a7ac8,#7aa8d8 50%,#8a5a36)"></div>
  <div class="name">Product Name</div>
  <div class="price"><span>$9.99</span><span class="old">$12.99</span></div>
  <div class="details btn-orange">Details</div>
</div>

<div class="abs rule-h"></div>
<div class="abs rule-v"></div>

<h2 class="abs video-title">Live Video Chat</h2>
<div class="abs video" role="img" aria-label="Video chat preview with the singer">
  <svg width="26" height="30"><path d="M0 0 L26 15 L0 30Z" fill="rgba(255,255,255,.45)"/></svg>
  <span>Click for Chat</span>
</div>

<h2 class="abs appt-title">Book An Appointment</h2>
<div class="abs calendar">
  <div class="head">November 2012</div>
  <div class="cal-grid">
    <span class="dow">M</span><span class="dow">T</span><span class="dow">W</span><span class="dow">T</span><span class="dow">F</span><span class="dow">S</span><span class="dow">S</span>
    <span>1</span><span>2</span><span>3</span><span>4</span><span>5</span><span>6</span><span>7</span>
    <span>8</span><span>9</span><span>10</span><span>11</span><span>12</span><span>13</span><span>14</span>
    <span>15</span><span>16</span><span>17</span><span>18</span><span>19</span><span>20</span><span>21</span>
    <span>22</span><span>23</span><span>24</span><span>25</span><span class="mark">26</span><span>27</span><span>28</span>
    <span>29</span><span class="mark">30</span><span>31</span>
  </div>
</div>

<footer>
  <div class="abs footer-col" style="left:99px;top:958px"><h3>Testimonials</h3></div>
  <p class="abs testimonial"><span class="quote">&ldquo;</span> Lorem ipsum dolor sit amet, consec tetuer adipiscing elit. Praesent vestibulum mo lestie lacus. Aenean nonummy hendrerit mauris. Phasellus porta.........</p>
  <div class="abs" style="left:100px;top:1055px;font-size:10px;font-style:italic;color:#eee">Continue Reading</div>
  <div class="abs" style="left:200px;width:114px;top:1055px;text-align:right;font-size:10px;font-style:italic;line-height:14px"><span style="color:var(--orange-hi)">Lena Morrow</span><br><span style="color:#aaa">5 days ago</span></div>
  <div class="abs f-line" style="left:100px;top:1098px;width:231px"></div>
  <div class="abs foot-link" style="left:100px;top:1106px">Read All Testimonials</div>
  <div class="abs f-line" style="left:100px;top:1125px;width:231px"></div>

  <div class="abs col-rule" style="left:352px"></div>

  <div class="abs footer-col" style="left:369px;top:958px"><h3>Latest News</h3></div>
  <div class="abs news-date" style="left:368px;top:984px">20<br>Nov</div>
  <p class="abs news-text" style="left:416px;top:986px">Lorem ipsum dolor sit amet, consec tetuer adipiscing elit.</p>
  <div class="abs f-line" style="left:369px;top:1030px;width:232px"></div>
  <div class="abs news-date" style="left:368px;top:1040px">19<br>Nov</div>
  <p class="abs news-text" style="left:416px;top:1042px">Lorem ipsum dolor sit amet, consec tetuer adipiscing elit.</p>
  <div class="abs f-line" style="left:369px;top:1098px;width:232px"></div>
  <div class="abs foot-link" style="left:369px;top:1106px">Read All Post</div>
  <div class="abs f-line" style="left:369px;top:1125px;width:232px"></div>

  <div class="abs col-rule" style="left:628px"></div>

  <div class="abs footer-col" style="left:646px;top:958px"><h3>Connect with me</h3></div>
  <div class="abs social" style="left:646px">Kinnect</div>
  <div class="abs social" style="left:688px">Chirpa</div>
  <div class="abs social" style="left:730px">Orbly</div>
  <div class="abs social" style="left:772px">ReelHub</div>
  <div class="abs footer-col" style="left:646px;top:1058px"><h3>Secure Payment with</h3></div>
  <div class="abs pay-badge">
    <div class="brand">PayVira</div>
    <div class="cards"><i></i><i></i><i></i><i></i></div>
  </div>

  <p class="abs copyright">Copyright &copy;2012 <b>Vanny-Kolthida</b><br>All Rights Reserved &nbsp;| &nbsp;Privacy Policy</p>
</footer>

</body>
</html>
```